Business Card with Logo and Company Name.

I would like a business card design that has both my logo and company name. The K7 logo was one part- now I would like the entire Company Name.

KESTRO CONTRACTING SERVICES

I have consulted with my team and we have went over several ideas for the last few weeks. We all love the K7 logo. Great for branding. What we have thought of in regards to the company name to tie into it is giving focus to font selection. We love the idea of KESTRO being a larger font and maybe making CONTRACTING SERVICES a larger font. Much like one would for a Slogan Line and font when designing.

I hope I’m communicating this correctly and not causing confusion. If need be I can mock up or sketch an idea and send. Just let me know.

**** I just noticed an area to upload an image. I uploaded one that was used as an idea*****

```html
<!DOCTYPE html>
<html lang="en">
<head>
<meta charset="utf-8">
<title>Kestro Contracting Services – Business Card</title>
<link href="https://fonts.googleapis.com/css2?family=Montserrat:wght@400;500;600;700&display=swap" rel="stylesheet">
<style>
  :root {
    --page: #e3e3e3;
    --paper: #ffffff;
    --rust: #ab5634;
    --rust-light: #b26443;
    --ink-light: #ffffff;
    --logo-silver: #e6e6e6;
  }
  * { margin: 0; padding: 0; box-sizing: border-box; }
  html, body {
    width: 1200px; height: 1200px; overflow: hidden;
    background: var(--page);
    font-family: "Montserrat", sans-serif;
  }
  .canvas { position: relative; width: 1200px; height: 1200px; }

  .card {
    position: absolute; left: 262px; width: 686px; height: 392px;
    box-shadow: 0 18px 26px rgba(0,0,0,0.18);
    overflow: hidden;
  }
  .card-front { top: 165px; background: var(--paper); }
  .card-back {
    top: 653px;
    background: linear-gradient(180deg, var(--rust-light) 0%, var(--rust) 100%);
  }

  /* Wordmark */
  .wordmark {
    position: absolute; left: 0; right: 0; text-align: center;
  }
  .wordmark-name {
    display: block;
    font-weight: 500; font-size: 70px; letter-spacing: 12px;
    line-height: 1; padding-left: 12px;
  }
  .wordmark-tagline {
    display: block; margin-top: 10px;
    font-weight: 500; font-size: 17px; letter-spacing: 2.4px;
  }
  .card-front .wordmark { top: 92px; color: var(--rust); }
  .card-back .wordmark { top: 146px; color: var(--logo-silver); }

  /* Front band */
  .contact-band {
    position: absolute; left: 0; right: 0; top: 224px; bottom: 0;
    background: var(--rust); color: var(--ink-light);
  }
  .person {
    position: absolute; right: calc(686px - 302px); top: 57px; text-align: right;
  }
  .person-name { font-weight: 700; font-size: 20.5px; letter-spacing: 0.8px; line-height: 1.2; }
  .person-role { font-weight: 400; font-size: 14.5px; letter-spacing: 0.6px; line-height: 1.2; }
  .divider {
    position: absolute; left: 321px; top: 39px; width: 1px; height: 84px;
    background: rgba(255,255,255,0.55);
  }
  .contact-list { position: absolute; left: 345px; top: 42px; list-style: none; }
  .contact-item {
    display: flex; align-items: flex-start;
    font-size: 14.5px; letter-spacing: 0.5px; line-height: 19px;
    margin-bottom: 4px;
  }
  .contact-item svg { width: 13px; height: 13px; margin-top: 3px; flex: none; fill: var(--ink-light); }
  .contact-text { margin-left: 6px; }

  /* Back website */
  .website {
    position: absolute; left: 0; right: 0; top: 335px; text-align: center;
    color: var(--ink-light); font-size: 14px; letter-spacing: 5px; font-weight: 400;
  }
  .website strong { font-weight: 600; }
</style>
</head>
<body>
<main class="canvas">

  <section class="card card-front" aria-label="Business card front">
    <div class="wordmark">
      <span class="wordmark-name">KESTRO</span>
      <span class="wordmark-tagline">Contracting Services</span>
    </div>

    <div class="contact-band">
      <div class="person">
        <div class="person-name">DANIEL HARLOW</div>
        <div class="person-role">President</div>
      </div>
      <div class="divider"></div>
      <ul class="contact-list">
        <li class="contact-item">
          <svg viewBox="0 0 24 24" aria-hidden="true"><path d="M12 1a8 8 0 0 0-8 8c0 6 8 14 8 14s8-8 8-14a8 8 0 0 0-8-8zm0 11a3 3 0 1 1 0-6 3 3 0 0 1 0 6z"/></svg>
          <span class="contact-text">4120 Birchwood Lane<br>Fairbanks, Alaska 99701</span>
        </li>
        <li class="contact-item">
          <svg viewBox="0 0 24 24" aria-hidden="true"><path d="M6.6 10.8a15.1 15.1 0 0 0 6.6 6.6l2.2-2.2a1 1 0 0 1 1-.25 11.4 11.4 0 0 0 3.6.57 1 1 0 0 1 1 1V20a1 1 0 0 1-1 1A17 17 0 0 1 3 4a1 1 0 0 1 1-1h3.5a1 1 0 0 1 1 1c0 1.25.2 2.45.57 3.57a1 1 0 0 1-.25 1z"/></svg>
          <span class="contact-text">555-014-2731</span>
        </li>
        <li class="contact-item">
          <svg viewBox="0 0 24 24" aria-hidden="true"><path d="M2 5h20v14H2z M2 5l10 8 10-8" fill="none" stroke="#fff" stroke-width="0"/><path d="M2 5h20v2l-10 7L2 7zM2 9l10 7 10-7v10H2z"/></svg>
          <span class="contact-text">info@kestro.com</span>
        </li>
      </ul>
    </div>
  </section>

  <section class="card card-back" aria-label="Business card back">
    <div class="wordmark">
      <span class="wordmark-name">KESTRO</span>
      <span class="wordmark-tagline">Contracting Services</span>
    </div>
    <div class="website">WWW.<strong>KESTRO</strong>.COM</div>
  </section>

</main>
</body>
</html>
```